Financial investment & advisory business needs a powerpoint design

We need a powerpoint design incorporating the logo (and colours) and relating to the business card design we already have. The company is a boutique financial investment and advisory business called Brevora Holdings Pty Ltd based in Australia. The final design should communicate innovative advice and financial safety and growth. A young, contemporary but experienced, professional business.

Target Market(s)

Companies listed or wishing to list on the Tarrowin Stock Exchange and Professional and Institutional Investors.

Industry/Entity Type

Finance

Requirements
Must have
• Incorporate the logo and colours. Be similar/relate to the business card design.
Nice to have
Should not have
• Do not deviate from the logo colours.
• Do not use black background or invert the logo.
• Do not deviate from the business card design too much.

```html
<!DOCTYPE html>
<html lang="en">
<head>
<meta charset="utf-8">
<title>Brevora Holdings – Presentation Template Overview</title>
<link href="https://fonts.googleapis.com/css2?family=Montserrat:wght@600;700&family=Open+Sans:wght@400;600&display=swap" rel="stylesheet">
<style>
  :root{
    --stage:#5b5b5b;
    --blue:#4a6fc4;
    --blue-dark:#2f4f9a;
    --blue-soft:#dfe6f5;
    --grey:#e9ebef;
    --grey-mid:#b9bec8;
    --ink:#555b66;
    --white:#ffffff;
  }
  *{box-sizing:border-box;margin:0;padding:0}
  html,body{width:805px;height:1200px;overflow:hidden;background:var(--stage)}
  .deck{
    position:absolute;left:64px;top:46px;
    display:grid;grid-template-columns:repeat(3,215px);grid-template-rows:repeat(8,121px);
    column-gap:16px;row-gap:20px;
  }
  .slide{position:relative;background:var(--white);overflow:hidden;font-family:"Open Sans",sans-serif;color:var(--ink)}
  .slide > *{position:absolute}
  .heading{font-family:"Montserrat",sans-serif;font-weight:700;font-size:5.5px;letter-spacing:.4px;color:var(--blue);text-transform:uppercase;left:0;right:0;top:8px;text-align:center;line-height:1.3}
  .heading-left{text-align:left;right:auto}
  .heading-white{color:var(--white)}
  .copy{font-size:3.8px;line-height:1.45;color:var(--ink)}
  .copy-white{color:var(--white)}
  .copy-center{text-align:center}
  .label{font-family:"Montserrat",sans-serif;font-size:4px;font-weight:600;color:var(--ink);line-height:1.3}
  .label-center{text-align:center}
  .label-white{color:var(--white)}
  .photo{background:linear-gradient(135deg,#8aa0c8,#c9d3e4 55%,#9aa6b6)}
  .photo-warm{background:linear-gradient(135deg,#c9a98a,#e6d6c4 50%,#8c95a8)}
  .photo-dark{background:linear-gradient(135deg,#26324a,#4a5a78 60%,#1c2436)}
  .round{border-radius:50%}
  .block-blue{background:var(--blue)}
  .block-grey{background:var(--grey)}
  .block-soft{background:var(--blue-soft)}
  .icon{width:14px;height:14px;border-radius:50%;background:var(--blue)}
  .icon svg{display:block}
  .cell{display:flex;align-items:center;justify-content:center;text-align:center}
  .wordmark{font-family:"Montserrat",sans-serif;font-weight:700;font-size:5px;color:var(--blue);display:flex;align-items:center;gap:3px}
  .wordmark i{display:block;width:6px;height:6px;background:var(--blue)}
  .title{font-family:"Montserrat",sans-serif;font-weight:700;color:var(--blue);font-size:10px;line-height:1.15}
</style>
</head>
<body>
<main class="deck">

  <!-- 1 cover -->
  <section class="slide">
    <div class="photo" role="img" aria-label="City skyline at sunrise" style="left:0;top:0;width:215px;height:121px"></div>
    <div class="block-blue" style="left:0;top:0;width:215px;height:16px;background:var(--blue-dark)"></div>
    <div class="wordmark" style="left:8px;top:5px;color:var(--white)"><i style="background:var(--white)"></i>BREVORA HOLDINGS</div>
    <div style="left:30px;top:30px;width:80px;height:62px;background:var(--white)"></div>
    <div class="title" style="left:40px;top:42px">EDIT TITLE<br>HERE</div>
    <div class="copy" style="left:40px;top:70px;width:64px">Investment and advisory presentation</div>
  </section>

  <!-- 2 about -->
  <section class="slide">
    <div class="heading">About Our Firm</div>
    <div class="block-blue" style="left:10px;top:24px;width:92px;height:86px"></div>
    <div class="label label-white" style="left:16px;top:31px;width:80px">Who We Are</div>
    <div class="copy copy-white" style="left:16px;top:40px;width:80px">Brevora Holdings is a boutique investment and advisory firm. We guide listed and growing companies with clear, independent advice built on safety and steady growth.</div>
    <div class="photo" role="img" aria-label="Glass office tower" style="left:108px;top:24px;width:97px;height:86px"></div>
  </section>

  <!-- 3 values -->
  <section class="slide">
    <div class="block-blue" style="left:0;top:0;width:70px;height:121px"></div>
    <div class="heading heading-left heading-white" style="left:8px;top:14px">Our Values</div>
    <div class="copy copy-white" style="left:8px;top:26px;width:56px">Four principles shape every piece of advice we give our clients.</div>
    <div class="icon" style="left:88px;top:22px"></div><div class="label" style="left:106px;top:24px">Trust</div>
    <div class="copy" style="left:106px;top:31px;width:40px">Honest advice always.</div>
    <div class="icon" style="left:152px;top:22px"></div><div class="label" style="left:170px;top:24px">Growth</div>
    <div class="copy" style="left:170px;top:31px;width:40px">Returns that last.</div>
    <div class="icon" style="left:88px;top:64px"></div><div class="label" style="left:106px;top:66px">Insight</div>
    <div class="copy" style="left:106px;top:73px;width:40px">Research led views.</div>
    <div class="icon" style="left:152px;top:64px"></div><div class="label" style="left:170px;top:66px">Safety</div>
    <div class="copy" style="left:170px;top:73px;width:40px">Capital protected.</div>
  </section>

  <!-- 4 team -->
  <section class="slide">
    <div class="heading">Our Team</div>
    <div class="photo round" role="img" aria-label="Team member portrait" style="left:44px;top:26px;width:30px;height:30px"></div>
    <div class="photo-warm round" role="img" aria-label="Team member portrait" style="left:93px;top:26px;width:30px;height:30px"></div>
    <div class="photo round" role="img" aria-label="Team member portrait" style="left:142px;top:26px;width:30px;height:30px"></div>
    <div class="label label-center" style="left:29px;top:62px;width:60px">Team Member</div>
    <div class="label label-center" style="left:78px;top:62px;width:60px">Team Member</div>
    <div class="label label-center" style="left:127px;top:62px;width:60px">Team Member</div>
    <div class="copy copy-center" style="left:29px;top:69px;width:60px">Director</div>
    <div class="copy copy-center" style="left:78px;top:69px;width:60px">Senior Adviser</div>
    <div class="copy copy-center" style="left:127px;top:69px;width:60px">Analyst</div>
    <div class="copy copy-center" style="left:24px;top:84px;width:167px">An experienced team bringing fresh thinking to capital markets, listings and investor relations.</div>
  </section>

  <!-- 5 services -->
  <section class="slide">
    <div class="heading">Our Services</div>
    <div class="icon" style="left:38px;top:24px"></div><div class="label label-center" style="left:20px;top:41px;width:50px">Equity Raising</div>
    <div class="icon" style="left:100px;top:24px"></div><div class="label label-center" style="left:82px;top:41px;width:50px">Advisory</div>
    <div class="icon" style="left:162px;top:24px"></div><div class="label label-center" style="left:144px;top:41px;width:50px">Listings</div>
    <div class="copy copy-center" style="left:20px;top:48px;width:50px">Capital for growth</div>
    <div class="copy copy-center" style="left:82px;top:48px;width:50px">Strategic guidance</div>
    <div class="copy copy-center" style="left:144px;top:48px;width:50px">Exchange ready</div>
    <div class="icon" style="left:38px;top:66px"></div><div class="label label-center" style="left:20px;top:83px;width:50px">Research</div>
    <div class="icon" style="left:100px;top:66px"></div><div class="label label-center" style="left:82px;top:83px;width:50px">Portfolios</div>
    <div class="icon" style="left:162px;top:66px"></div><div class="label label-center" style="left:144px;top:83px;width:50px">Risk Review</div>
    <div class="copy copy-center" style="left:20px;top:90px;width:50px">Sector insight</div>
    <div class="copy copy-center" style="left:82px;top:90px;width:50px">Managed wealth</div>
    <div class="copy copy-center" style="left:144px;top:90px;width:50px">Capital safety</div>
  </section>

  <!-- 6 profile -->
  <section class="slide">
    <div class="photo" role="img" aria-label="Modern office building" style="left:0;top:0;width:84px;height:121px"></div>
    <div class="heading heading-left" style="left:96px;top:16px">Company Profile</div>
    <div class="copy" style="left:96px;top:28px;width:108px">Founded by seasoned advisers, we support companies listed or preparing to list on the Tarrowin Stock Exchange, as well as professional and institutional investors seeking sound opportunities.</div>
    <div class="block-blue cell" style="left:96px;top:96px;width:108px;height:12px"><span class="label label-white">Independent. Trusted. Focused.</span></div>
  </section>

  <!-- 7 experience -->
  <section class="slide">
    <div class="heading">Our Experience</div>
    <div class="photo-warm" role="img" aria-label="Colleagues meeting in office" style="left:10px;top:22px;width:88px;height:88px"></div>
    <div class="block-blue" style="left:108px;top:26px;width:20px;height:20px"></div><div class="label" style="left:134px;top:27px">Plan</div><div class="copy" style="left:134px;top:34px;width:72px">Set clear objectives.</div>
    <div class="block-blue" style="left:108px;top:56px;width:20px;height:20px"></div><div class="label" style="left:134px;top:57px">Invest</div><div class="copy" style="left:134px;top:64px;width:72px">Deploy capital wisely.</div>
    <div class="block-blue" style="left:108px;top:86px;width:20px;height:20px"></div><div class="label" style="left:134px;top:87px">Grow</div><div class="copy" style="left:134px;top:94px;width:72px">Build lasting value.</div>
  </section>

  <!-- 8 strengths -->
  <section class="slide">
    <div class="heading">Our Strengths</div>
    <div class="block-blue" style="left:10px;top:22px;width:45px;height:90px"></div>
    <div class="block-blue" style="left:59px;top:22px;width:45px;height:90px"></div>
    <div class="block-blue" style="left:108px;top:22px;width:45px;height:90px"></div>
    <div class="block-blue" style="left:157px;top:22px;width:45px;height:90px"></div>
    <div class="photo" role="img" aria-label="Business scene" style="left:10px;top:22px;width:45px;height:32px"></div>
    <div class="photo-warm" role="img" aria-label="Business scene" style="left:59px;top:22px;width:45px;height:32px"></div>
    <div class="photo" role="img" aria-label="Business scene" style="left:108px;top:22px;width:45px;height:32px"></div>
    <div class="photo-warm" role="img" aria-label="Business scene" style="left:157px;top:22px;width:45px;height:32px"></div>
    <div class="label label-white" style="left:14px;top:60px">Expertise</div>
    <div class="label label-white" style="left:63px;top:60px">Network</div>
    <div class="label label-white" style="left:112px;top:60px">Discipline</div>
    <div class="label label-white" style="left:161px;top:60px">Results</div>
    <div class="copy copy-white" style="left:14px;top:68px;width:38px">Decades of market know-how.</div>
    <div class="copy copy-white" style="left:63px;top:68px;width:38px">Strong investor relationships.</div>
    <div class="copy copy-white" style="left:112px;top:68px;width:38px">Careful, tested process.</div>
    <div class="copy copy-white" style="left:161px;top:68px;width:38px">Proven client outcomes.</div>
  </section>

  <!-- 9 board -->
  <section class="slide">
    <div class="heading">Meet The Board</div>
    <div class="block-blue" style="left:0;top:46px;width:215px;height:52px"></div>
    <div class="photo-warm round" role="img" aria-label="Board member portrait" style="left:44px;top:30px;width:34px;height:34px;border:2px solid var(--white)"></div>
    <div class="photo round" role="img" aria-label="Board member portrait" style="left:91px;top:30px;width:34px;height:34px;border:2px solid var(--white)"></div>
    <div class="photo-warm round" role="img" aria-label="Board member portrait" style="left:138px;top:30px;width:34px;height:34px;border:2px solid var(--white)"></div>
    <div class="label label-white label-center" style="left:36px;top:70px;width:50px">Chairman</div>
    <div class="label label-white label-center" style="left:83px;top:70px;width:50px">Director</div>
    <div class="label label-white label-center" style="left:130px;top:70px;width:50px">Director</div>
    <div class="copy copy-white copy-center" style="left:36px;top:77px;width:50px">Board member</div>
    <div class="copy copy-white copy-center" style="left:83px;top:77px;width:50px">Board member</div>
    <div class="copy copy-white copy-center" style="left:130px;top:77px;width:50px">Board member</div>
  </section>

  <!-- 10 client focus -->
  <section class="slide">
    <div class="photo-warm" role="img" aria-label="Professional woman smiling" style="left:10px;top:14px;width:70px;height:96px"></div>
    <div class="heading heading-left" style="left:92px;top:18px">Client Focus</div>
    <div class="copy" style="left:92px;top:30px;width:112px">Every recommendation starts with our client's goals. We listen first, then shape advice that protects capital and creates room for growth.</div>
    <div class="copy" style="left:92px;top:62px;width:112px">Long-term partnerships, clear reporting and open conversations define how we work.</div>
  </section>

  <!-- 11 strategy -->
  <section class="slide">
    <div class="block-blue" style="left:0;top:0;width:215px;height:40px"></div>
    <div class="heading heading-white" style="top:13px">Strategic Advice For Sustainable<br>Financial Growth</div>
    <div class="icon" style="left:34px;top:52px"></div><div class="label label-center" style="left:21px;top:69px;width:40px">Plan</div>
    <div class="icon" style="left:80px;top:52px"></div><div class="label label-center" style="left:67px;top:69px;width:40px">Review</div>
    <div class="icon" style="left:126px;top:52px"></div><div class="label label-center" style="left:113px;top:69px;width:40px">Report</div>
    <div class="icon" style="left:172px;top:52px"></div><div class="label label-center" style="left:159px;top:69px;width:40px">Grow</div>
    <div class="copy copy-center" style="left:20px;top:86px;width:175px">A structured approach that keeps every client on track toward measurable results.</div>
  </section>

  <!-- 12 case studies -->
  <section class="slide">
    <div class="heading">Case Studies</div>
    <div class="block-blue" style="left:10px;top:24px;width:16px;height:16px"></div><div class="label" style="left:31px;top:25px">IPO Listing</div><div class="copy" style="left:31px;top:32px">Raised growth capital</div>
    <div class="block-blue" style="left:10px;top:46px;width:16px;height:16px"></div><div class="label" style="left:31px;top:47px">Merger</div><div class="copy" style="left:31px;top:54px">Advised on deal terms</div>
    <div class="block-blue" style="left:10px;top:68px;width:16px;height:16px"></div><div class="label" style="left:31px;top:69px">Placement</div><div class="copy" style="left:31px;top:76px">Institutional support</div>
    <div class="block-blue" style="left:10px;top:90px;width:16px;height:16px"></div><div class="label" style="left:31px;top:91px">Restructure</div><div class="copy" style="left:31px;top:98px">Balance sheet repair</div>
    <div class="photo-warm" role="img" aria-label="Team at a meeting table" style="left:104px;top:24px;width:101px;height:82px"></div>
  </section>

  <!-- 13 comparison -->
  <section class="slide">
    <div class="heading">Comparison</div>
    <div class="block-grey cell label" style="left:12px;top:22px;width:92px;height:12px">Option A</div>
    <div class="block-blue cell label label-white" style="left:111px;top:22px;width:92px;height:12px">Option B</div>
    <div class="block-grey cell copy" style="left:12px;top:38px;width:92px;height:11px">Lower upfront cost</div><div class="block-grey cell copy" style="left:111px;top:38px;width:92px;height:11px">Higher growth potential</div>
    <div class="block-grey cell copy" style="left:12px;top:53px;width:92px;height:11px">Short time frame</div><div class="block-grey cell copy" style="left:111px;top:53px;width:92px;height:11px">Long time frame</div>
    <div class="block-grey cell copy" style="left:12px;top:68px;width:92px;height:11px">Fixed returns</div><div class="block-grey cell copy" style="left:111px;top:68px;width:92px;height:11px">Market linked returns</div>
    <div class="block-grey cell copy" style="left:12px;top:83px;width:92px;height:11px">Low risk profile</div><div class="block-grey cell copy" style="left:111px;top:83px;width:92px;height:11px">Balanced risk profile</div>
  </section>

  <!-- 14 structure -->
  <section class="slide">
    <div class="heading">Structure</div>
    <svg style="left:0;top:0" width="215" height="121" viewBox="0 0 215 121">
      <g fill="none" stroke="#b9bec8" stroke-width="1">
        <path d="M107.5 34 V44 M55 50 H82 M133 50 H160 M55 72 H82 M133 72 H160 M55 94 H82 M133 94 H160 M107.5 56 V66 M107.5 78 V88"/>
      </g>
      <g fill="#4a6fc4">
        <rect x="14" y="44" width="41" height="12"/><rect x="82" y="44" width="51" height="12"/><rect x="160" y="44" width="41" height="12"/>
        <rect x="14" y="66" width="41" height="12"/><rect x="82" y="66" width="51" height="12"/><rect x="160" y="66" width="41" height="12"/>
        <rect x="14" y="88" width="41" height="12"/><rect x="82" y="88" width="51" height="12"/><rect x="160" y="88" width="41" height="12"/>
      </g>
      <rect x="82" y="22" width="51" height="12" fill="#2f4f9a"/>
      <g font-family="Montserrat, sans-serif" font-size="4" font-weight="600" fill="#ffffff" text-anchor="middle">
        <text x="107.5" y="29.5">Board</text>
        <text x="34.5" y="51.5">Finance</text><text x="107.5" y="51.5">Managing Director</text><text x="180.5" y="51.5">Legal</text>
        <text x="34.5" y="73.5">Research</text><text x="107.5" y="73.5">Advisory</text><text x="180.5" y="73.5">Compliance</text>
        <text x="34.5" y="95.5">Analysts</text><text x="107.5" y="95.5">Client Service</text><text x="180.5" y="95.5">Operations</text>
      </g>
    </svg>
  </section>

  <!-- 15 outlook -->
  <section class="slide">
    <div class="photo" role="img" aria-label="Bridge over harbour water" style="left:0;top:0;width:215px;height:121px;background:linear-gradient(160deg,#3f66be,#7f9bd6 55%,#2f4f9a)"></div>
    <div style="left:14px;top:14px;width:86px;height:40px;background:var(--white)"></div>
    <div class="heading heading-left" style="left:20px;top:21px">Market Outlook</div>
    <div class="copy" style="left:20px;top:31px;width:74px">Steady growth expected across key sectors this year.</div>
  </section>

  <!-- 16 process -->
  <section class="slide">
    <div class="heading">Our Process</div>
    <div class="block-blue cell label label-white" style="left:14px;top:22px;width:42px;height:18px">Step 01</div><div class="block-grey copy" style="left:62px;top:22px;width:140px;height:18px;padding:3px 6px">Discovery meeting to understand goals, risk and timing.</div>
    <div class="block-blue cell label label-white" style="left:14px;top:44px;width:42px;height:18px">Step 02</div><div class="block-grey copy" style="left:62px;top:44px;width:140px;height:18px;padding:3px 6px">Research and analysis of markets and opportunities.</div>
    <div class="block-blue cell label label-white" style="left:14px;top:66px;width:42px;height:18px">Step 03</div><div class="block-grey copy" style="left:62px;top:66px;width:140px;height:18px;padding:3px 6px">Tailored strategy presented with clear recommendations.</div>
    <div class="block-blue cell label label-white" style="left:14px;top:88px;width:42px;height:18px">Step 04</div><div class="block-grey copy" style="left:62px;top:88px;width:140px;height:18px;padding:3px 6px">Ongoing review, reporting and portfolio adjustment.</div>
  </section>

  <!-- 17 partnership -->
  <section class="slide">
    <div class="heading">Partnership</div>
    <div class="photo-warm" role="img" aria-label="Business handshake" style="left:10px;top:22px;width:110px;height:88px"></div>
    <div class="block-blue" style="left:120px;top:30px;width:85px;height:72px"></div>
    <div class="label label-white" style="left:128px;top:38px">Working Together</div>
    <div class="copy copy-white" style="left:128px;top:47px;width:70px">We build close partnerships with management teams and investors, sharing insight and aligning goals for long-term growth.</div>
  </section>

  <!-- 18 people -->
  <section class="slide">
    <div class="heading">Our People</div>
    <div class="block-blue" style="left:0;top:26px;width:215px;height:58px"></div>
    <div class="photo-warm" role="img" aria-label="Group of colleagues" style="left:108px;top:30px;width:100px;height:50px"></div>
    <div class="label label-white" style="left:12px;top:34px">A Young, Skilled Team</div>
    <div class="copy copy-white" style="left:12px;top:43px;width:88px">Contemporary thinking backed by real experience across finance and capital markets.</div>
    <div class="copy copy-center" style="left:12px;top:92px;width:191px">Our advisers combine modern tools with proven judgement.</div>
  </section>

  <!-- 19 offices -->
  <section class="slide">
    <div class="heading">Our Offices</div>
    <div class="photo" role="img" aria-label="Office interior" style="left:10px;top:22px;width:48px;height:40px"></div>
    <div class="photo-warm" role="img" aria-label="Team portrait" style="left:62px;top:22px;width:48px;height:40px"></div>
    <div class="photo-warm" role="img" aria-label="Client meeting" style="left:10px;top:66px;width:100px;height:44px"></div>
    <div class="label" style="left:120px;top:24px">Head Office</div>
    <div class="copy" style="left:120px;top:32px;width:86px">Modern workspaces designed for focused client meetings and research.</div>
    <div class="block-blue cell label label-white" style="left:120px;top:94px;width:84px;height:12px">Visit Us</div>
  </section>

  <!-- 20 summary table -->
  <section class="slide">
    <div class="heading">Financial Summary</div>
    <svg style="left:12px;top:22px" width="191" height="80" viewBox="0 0 191 80">
      <rect width="191" height="12" fill="#4a6fc4"/>
      <rect y="14" width="191" height="11" fill="#e9ebef"/>
      <rect y="27" width="191" height="11" fill="#dfe6f5"/>
      <rect y="40" width="191" height="11" fill="#e9ebef"/>
      <rect y="53" width="191" height="11" fill="#dfe6f5"/>
      <rect y="66" width="191" height="11" fill="#e9ebef"/>
      <g font-family="Montserrat, sans-serif" font-size="4" font-weight="600" fill="#ffffff">
        <text x="6" y="7.5">Item</text><text x="80" y="7.5">2022</text><text x="120" y="7.5">2023</text><text x="160" y="7.5">2024</text>
      </g>
      <g font-family="Open Sans, sans-serif" font-size="3.8" fill="#555b66">
        <text x="6" y="21">Revenue</text><text x="80" y="21">$2.4m</text><text x="120" y="21">$3.1m</text><text x="160" y="21">$3.9m</text>
        <text x="6" y="34">Expenses</text><text x="80" y="34">$1.6m</text><text x="120" y="34">$1.9m</text><text x="160" y="34">$2.2m</text>
        <text x="6" y="47">Net Profit</text><text x="80" y="47">$0.8m</text><text x="120" y="47">$1.2m</text><text x="160" y="47">$1.7m</text>
        <text x="6" y="60">Assets</text><text x="80" y="60">$5.2m</text><text x="120" y="60">$6.0m</text><text x="160" y="60">$7.1m</text>
        <text x="6" y="73">Clients</text><text x="80" y="73">48</text><text x="120" y="73">61</text><text x="160" y="73">77</text>
      </g>
    </svg>
  </section>

  <!-- 21 key figures -->
  <section class="slide">
    <div class="heading">Key Figures</div>
    <div class="block-blue cell label label-white" style="left:14px;top:26px;width:20px;height:20px">01</div><div class="label" style="left:38px;top:28px">$40m</div><div class="copy" style="left:38px;top:35px">Capital raised</div>
    <div class="block-blue cell label label-white" style="left:78px;top:26px;width:20px;height:20px">02</div><div class="label" style="left:102px;top:28px">120+</div><div class="copy" style="left:102px;top:35px">Investors</div>
    <div class="block-blue cell label label-white" style="left:142px;top:26px;width:20px;height:20px">03</div><div class="label" style="left:166px;top:28px">15</div><div class="copy" style="left:166px;top:35px">Listings</div>
    <div class="block-blue cell label label-white" style="left:14px;top:66px;width:20px;height:20px">04</div><div class="label" style="left:38px;top:68px">98%</div><div class="copy" style="left:38px;top:75px">Retention</div>
    <div class="block-blue cell label label-white" style="left:78px;top:66px;width:20px;height:20px">05</div><div class="label" style="left:102px;top:68px">12 yrs</div><div class="copy" style="left:102px;top:75px">Experience</div>
    <div class="block-blue cell label label-white" style="left:142px;top:66px;width:20px;height:20px">06</div><div class="label" style="left:166px;top:68px">6</div><div class="copy" style="left:166px;top:75px">Sectors</div>
  </section>

  <!-- 22 contact -->
  <section class="slide">
    <div class="photo-dark" role="img" aria-label="Evening city view" style="left:0;top:0;width:215px;height:121px"></div>
    <div class="round" style="left:40px;top:34px;width:36px;height:36px;background:var(--white)"></div>
    <div class="label label-white label-center" style="left:18px;top:76px;width:80px">BREVORA HOLDINGS</div>
    <div class="heading heading-left heading-white" style="left:110px;top:28px">Contact Us</div>
    <div class="icon" style="left:110px;top:42px;width:9px;height:9px"></div><div class="copy copy-white" style="left:124px;top:43px">+61 2 5550 1234</div>
    <div class="icon" style="left:110px;top:58px;width:9px;height:9px"></div><div class="copy copy-white" style="left:124px;top:59px">hello@brevora.example</div>
    <div class="icon" style="left:110px;top:74px;width:9px;height:9px"></div><div class="copy copy-white" style="left:124px;top:75px">www.brevora.example</div>
  </section>

  <!-- 23 reach -->
  <section class="slide">
    <div class="heading">Our Reach</div>
    <div role="img" aria-label="Map of Australia showing office locations" style="left:50px;top:22px;width:115px;height:78px;background:linear-gradient(135deg,#eceef2,#c9ced7);border:1px solid var(--grey-mid)"></div>
    <div class="copy copy-center" style="left:20px;top:104px;width:175px">Advising clients in every state and territory.</div>
  </section>

  <!-- 24 thank you -->
  <section class="slide">
    <div class="block-blue" style="left:0;top:0;width:84px;height:121px"></div>
    <div class="title" style="left:12px;top:52px;color:var(--white);font-size:8px">THANK YOU</div>
    <div class="copy copy-white" style="left:12px;top:64px;width:64px">We look forward to working with you.</div>
    <div class="photo-warm" role="img" aria-label="Smiling business team" style="left:84px;top:0;width:131px;height:121px"></div>
  </section>

</main>
</body>
</html>
```